Flyer-Design für Unternehmen mit Fokus auf 3D-Messtechnik
Zielgruppe
Deutsch:
Wir sind ein Ingenieur Dienstleistungsunternehmen mit Fokus auf 3D-Messtechnik und zerstörungsfreier Prüftechnik mit kamerabasierten Systemen. Wir entwickeln Prüfalgorithmen zur automatisierten Bauteilinspektion.
Unsere Zielgruppe sind produzierende Unternehmen die ihre Qualitätskontrolle durch optische Prüfsysteme ergänzen und/oder komplexe Bauteilmessungen bei einem Dienstleister outsourcen möchten.
Englisch:
We are an engineering service company with focus on 3D measurement and non destructive testing with camera systems. We develop inspection algorithms regarding automated quality check of components. Our target group are producing companies which want to perform there quality checks by optical inspection systems and/or want to have high precise measurements of there parts.
Aufgabenstellung
The flyer should give a good overview of the companies services. The format can be 6 pages and high side but you can also be creative if another format matches well. The different business areas are:
1. 3D-Messtechnik
2. Zerstörungsfreie Prüftechnik mit bildgebenden Systemen
3. Softwareentwicklung mit Schwerpunkt optische Qualitätskontrolle
4. Machbarkeitsstudien
5. Schulungen
A first draft of content i have uploaded in a word document, please just insert it i can edit it later.
To every of the 5 business areas suggestions of pictures can be made, also from stock pictures. I will have a look in parallel.

```html
<!DOCTYPE html>
<html lang="de">
<head>
<meta charset="utf-8">
<title>OPTIKON WERK – Flyer</title>
<link href="https://fonts.googleapis.com/css2?family=Open+Sans:wght@400;600;700;800&display=swap" rel="stylesheet">
<style>
  :root {
    --navy: #1c3a6b;
    --navy-deep: #142c55;
    --ink: #2b2f36;
    --paper: #ffffff;
    --stage: #eef0f3;
    --line: #ffffff;
  }
  * { box-sizing: border-box; margin: 0; padding: 0; }
  html, body { width: 981px; height: 1200px; overflow: hidden; }
  body {
    background: var(--stage);
    font-family: "Open Sans", Arial, sans-serif;
    color: var(--ink);
    position: relative;
  }
  .spread {
    position: absolute;
    display: flex;
    box-shadow: 0 6px 18px rgba(0,0,0,.18);
  }
  .spread--outside { left: 55px; top: 60px; }
  .spread--inside  { left: 55px; top: 420px; }
  .single { position: absolute; top: 810px; box-shadow: 0 6px 18px rgba(0,0,0,.18); }
  .single--cover { left: 170px; }
  .single--back  { left: 520px; }

  .panel {
    position: relative;
    width: 290px;
    height: 300px;
    background: var(--paper);
    overflow: hidden;
  }
  .panel-title {
    font-weight: 800;
    color: var(--navy);
    font-size: 22px;
    line-height: 1.02;
    letter-spacing: .3px;
    text-transform: uppercase;
  }
  .panel-text {
    font-size: 7.6px;
    line-height: 1.32;
    color: var(--ink);
  }

  /* Software */
  .software-photo {
    position: absolute; left: 0; top: 0; width: 95px; height: 300px;
    background: linear-gradient(100deg, #0f3f7a 0%, #1b5a9c 55%, #124280 100%);
  }
  .software-body { position: absolute; left: 110px; top: 28px; right: 14px; }
  .software-body .panel-title { font-size: 20px; margin-bottom: 12px; }

  /* Schulung */
  .training-body { position: absolute; left: 22px; top: 38px; right: 22px; }
  .training-body .panel-title { margin-bottom: 14px; }
  .contact-band {
    position: absolute; left: 0; right: 0; top: 190px; bottom: 0;
    background: var(--navy);
    color: #fff;
    text-align: center;
    padding-top: 38px;
    font-size: 7.2px;
    line-height: 1.45;
  }
  .contact-band strong { font-weight: 700; display: block; }
  .contact-icon {
    position: absolute; left: 50%; top: 165px;
    width: 50px; height: 50px; margin-left: -25px;
    border-radius: 50%;
    background: #fff;
    border: 2px solid var(--navy);
    display: flex; align-items: center; justify-content: center;
  }

  /* Cover */
  .cover-photo {
    position: absolute; left: 0; top: 0; right: 0; height: 205px;
    background: radial-gradient(circle at 40% 40%, #b59a86 0%, #8a7a74 35%, #56606e 75%, #3d4a5c 100%);
  }
  .brand {
    position: absolute; left: 0; right: 0; top: 112px;
    display: flex; align-items: center; justify-content: center; gap: 10px;
    color: #fff; font-weight: 600; font-size: 22px; letter-spacing: 2px;
  }
  .brand-square { width: 16px; height: 16px; background: #fff; border-radius: 3px; }
  .cover-band {
    position: absolute; left: 0; right: 0; top: 208px; bottom: 0;
    background: var(--navy); color: #fff;
    padding: 22px 26px 0;
  }
  .cover-band h2 { font-size: 13.5px; font-weight: 800; letter-spacing: .3px; margin-bottom: 8px; }
  .cover-band p { font-size: 8px; line-height: 1.35; }

  /* Messtechnik */
  .measure-body { position: absolute; left: 22px; top: 24px; right: 22px; }
  .measure-body .panel-title { margin-bottom: 8px; }
  .express-area {
    position: absolute; left: 0; right: 0; top: 148px; bottom: 0;
    background: linear-gradient(160deg, #2c4a7d 0%, #1f3e71 60%, #223a64 100%);
  }
  .express-frame {
    position: absolute; left: 40px; right: 40px; top: 26px; height: 100px;
    border: 1px solid rgba(255,255,255,.85);
    color: #fff; text-align: center;
    padding: 34px 10px 0;
  }
  .express-frame h3 { font-size: 10px; font-weight: 700; margin-bottom: 5px; letter-spacing: .3px; }
  .express-frame p { font-size: 7.4px; line-height: 1.3; }
  .express-icon {
    position: absolute; left: 50%; top: 2px; margin-left: -24px;
    width: 48px; height: 48px; border-radius: 50%;
    background: #fff; border: 2px solid var(--navy);
    display: flex; align-items: center; justify-content: center;
  }

  /* Prüftechnik */
  .machine-photo {
    position: absolute; left: 0; top: 0; right: 0; height: 150px;
    background: linear-gradient(135deg, #2e4f82 0%, #4a6a9a 45%, #2a4576 100%);
  }
  .testing-body { position: absolute; left: 22px; top: 165px; right: 20px; }
  .testing-body .panel-title { font-size: 20px; margin-bottom: 8px; }

  /* Machbarkeit */
  .study-body { position: absolute; left: 20px; top: 26px; right: 16px; }
  .study-body .panel-title { font-size: 19.5px; margin-bottom: 8px; letter-spacing: 0; }
  .lens-photo {
    position: absolute; left: 0; right: 0; top: 165px; bottom: 0;
    background: linear-gradient(90deg, #3b3e44 0%, #cfd2d6 40%, #8a8e94 65%, #e9eaec 100%);
  }
</style>
</head>
<body>

<!-- Outside spread -->
<section class="spread spread--outside">
  <article class="panel panel--software">
    <div class="software-photo" role="img" aria-label="Blau getöntes Foto von Programmcode auf einem Bildschirm"></div>
    <div class="software-body">
      <h2 class="panel-title">Software-<br>entwicklung</h2>
      <p class="panel-text">Wir entwickeln Software mit Fokus auf Computer Vision Applikationen. Dazu verwenden wir eine geschwindigkeitsoptimierte Bildverarbeitungsbibliothek kombiniert mit selbst entwickelten Algorithmen. Die Kameraanbindung sowie Beleuchtungsansteuerung erfolgen in der hauseigenen Software, sie erhalten also die Computer Vision Funktionalität aus einer Hand.</p>
    </div>
  </article>

  <article class="panel panel--training">
    <div class="training-body">
      <h2 class="panel-title">Schulung und<br>Beratung</h2>
      <p class="panel-text">Benötigen Sie Unterstützung bei der Programmierung Ihrer Kastell Messmaschine unter QMetrix oder im Bereich der digitalen Bildverarbeitung? Kontaktieren Sie uns und wir besprechen die weitere Vorgehensweise um Sie optimal zu unterstützen.</p>
    </div>
    <div class="contact-band">
      OPTIKON WERK GbR • Talbergweg 12-14 • 58000 Musterstadt
      <strong>IHR ANSPRECHPARTNER:</strong>
      Dr.-Ing. Jonas Feldt • kontakt@optikon-werk.de • Tel: +49 151 000 111 22<br>
      www.optikon-werk.de
    </div>
    <div class="contact-icon">
      <svg width="28" height="24" viewBox="0 0 28 24" fill="none" stroke="#1c3a6b" stroke-width="1.4" stroke-linejoin="round">
        <rect x="11" y="3" width="15" height="10" rx="1"/>
        <path d="M11 3 L18.5 9 L26 3"/>
        <path d="M4 8 c-2 2 -2 6 2 10 c4 4 7 4 9 2 l-2.5-3 -2 1 c-2-1-4-3-5-5 l1-2 -2.5-3z"/>
      </svg>
    </div>
  </article>

  <article class="panel panel--cover">
    <div class="cover-photo" role="img" aria-label="Unscharfes Foto einer Büroszene in warmen Tönen"></div>
    <div class="brand"><span class="brand-square"></span>OPTIKON WERK</div>
    <div class="cover-band">
      <h2>IHR KOMPETENTER PARTNER.</h2>
      <p>Im Bereich 3D-Messtechnik und<br>der zerstörungsfreien Prüftechnik.</p>
    </div>
  </article>
</section>

<!-- Inside spread -->
<section class="spread spread--inside">
  <article class="panel panel--measure">
    <div class="measure-body">
      <h2 class="panel-title">Messtechnik</h2>
      <p class="panel-text">Wir vermessen Ihre Bauteile entsprechend Ihren Anforderungen mit modernen Messmaschinen entweder optisch, taktil oder in Kombination der beiden Verfahren. Die Messungen werden ausschließlich in einem klimatisierten Messraum vorgenommen. Der Messbericht kann in verschiedenen Formaten z.B. als Text,- CSV,- oder Exceldatei geliefert werden und ist natürlich entsprechend Ihren Anforderungen formatierbar.</p>
    </div>
    <div class="express-area" role="img" aria-label="Blau getöntes Foto eines Messtasters an einem Bauteil">
      <div class="express-frame">
        <h3>EXPRESS-SERVICE</h3>
        <p>Benötigen Sie schnell Ihre Messergebnisse rufen Sie uns an, wir vereinbaren umgehend einen Termin um Ihre Bauteile abzuholen.</p>
      </div>
      <div class="express-icon">
        <svg width="24" height="24" viewBox="0 0 24 24" fill="none" stroke="#1c3a6b" stroke-width="1.6" stroke-linecap="round" stroke-linejoin="round">
          <path d="M5 19 L19 5"/><path d="M10 5 H19 V14"/>
        </svg>
      </div>
    </div>
  </article>

  <article class="panel panel--testing">
    <div class="machine-photo" role="img" aria-label="Blau getöntes Foto einer Inspektionsanlage mit Kamera"></div>
    <div class="testing-body">
      <h2 class="panel-title">Zerstörungsfreie<br>Prüftechnik</h2>
      <p class="panel-text">Sind Sie an einem Inspektionssystem zur optischen Qualitätskontrolle Ihrer Bauteile interessiert? Wir entwickeln das System entsprechend Ihren Anforderungen, von einem manuellen Inspektionsarbeitsplatz bis hin zu einer automatisierten Defekterkennung. Mit Hilfe unserer umfangreichen Computer Vision Bibliothek erhalten Sie modernste Bildverarbeitungsfunktionen.</p>
    </div>
  </article>

  <article class="panel panel--study">
    <div class="study-body">
      <h2 class="panel-title">Machbakeitsstudien</h2>
      <p class="panel-text">Haben Sie ein Automatisierungsvorhaben im Fokus aber möchten zunächst herausarbeiten welche Computer Vision Technologien am besten für das Projekt geeignet sind? Mit welchem zeitlichen Umfang und Budget zu rechnen ist? Wie prozesssicher kann eine automatische Bildauswertung für das Projekt eingeordnet werden? Gerne führen wir eine Studie für Sie durch, dafür stehen unterschiedliche Kameras, Objektive, Filter und Beleuchtungsmodule zur Verfügung.</p>
    </div>
    <div class="lens-photo" role="img" aria-label="Foto mehrerer Kameraobjektive auf hellem Grund"></div>
  </article>
</section>

<!-- Single pages -->
<article class="panel panel--cover single single--cover">
  <div class="cover-photo" role="img" aria-label="Unscharfes Foto einer Büroszene in warmen Tönen"></div>
  <div class="brand"><span class="brand-square"></span>OPTIKON WERK</div>
  <div class="cover-band">
    <h2>IHR KOMPETENTER PARTNER.</h2>
    <p>Im Bereich 3D-Messtechnik und<br>der zerstörungsfreien Prüftechnik.</p>
  </div>
</article>

<article class="panel panel--training single single--back">
  <div class="training-body">
    <h2 class="panel-title">Schulung und<br>Beratung</h2>
    <p class="panel-text">Benötigen Sie Unterstützung bei der Programmierung Ihrer Kastell Messmaschine unter QMetrix oder im Bereich der digitalen Bildverarbeitung? Kontaktieren Sie uns und wir besprechen die weitere Vorgehensweise um Sie optimal zu unterstützen.</p>
  </div>
  <div class="contact-band">
    OPTIKON WERK GbR • Talbergweg 12-14 • 58000 Musterstadt
    <strong>IHR ANSPRECHPARTNER:</strong>
    Dr.-Ing. Jonas Feldt • kontakt@optikon-werk.de • Tel: +49 151 000 111 22<br>
    www.optikon-werk.de
  </div>
  <div class="contact-icon">
    <svg width="28" height="24" viewBox="0 0 28 24" fill="none" stroke="#1c3a6b" stroke-width="1.4" stroke-linejoin="round">
      <rect x="11" y="3" width="15" height="10" rx="1"/>
      <path d="M11 3 L18.5 9 L26 3"/>
      <path d="M4 8 c-2 2 -2 6 2 10 c4 4 7 4 9 2 l-2.5-3 -2 1 c-2-1-4-3-5-5 l1-2 -2.5-3z"/>
    </svg>
  </div>
</article>

</body>
</html>
```